Design for new site

Hi, we need a web design for a new product stillharborway.
This product is aimed to help people with anxiety, panic attacks and other disorders on permanently basis.
Please take a look at competitors web-sites:
http://www.quietlanternmethod.example/
http://www.brightmoorcalm.example/
Key Audiences
The intended audience for this site will be people that are looking for relief from panic and anxiety.
Key Objectives
Key object is to get prospective clients to sign up for membership and purchase our audio course.
Theme of Site
The general site theme needs to be clean and simple. The audience coming to the site in under a lot of anxiety and we don’t want to add any stress.
The site needs to flow easy from top down, with few distractions in side menus and/or columns.
Color Scheme
Suggested colors need to be light shades of blue. Blue psychology is tranquil, peaceful, and calm. This color has a tremendous stress management quality to it, making us feel cool and calm.
Or it can be shades of cool green of summer forest.
Please take a look at site mock up in attachment.

```html
<!DOCTYPE html>
<html lang="en">
<head>
<meta charset="utf-8">
<title>StillHarbor Way</title>
<link href="https://fonts.googleapis.com/css2?family=Montserrat:wght@700&family=Open+Sans:ital,wght@0,400;0,600;0,700;1,400&display=swap" rel="stylesheet">
<style>
:root{
  --sky:#35c8fb;
  --accent:#2bb6e6;
  --nav:#353535;
  --ink:#333333;
  --body:#7a7a7a;
  --muted:#8a8a8a;
  --rule:#e2e2e2;
  --panel:#f6f6f6;
  --footer:#1c1c1c;
  --white:#ffffff;
}
*{margin:0;padding:0;box-sizing:border-box}
html,body{width:908px;height:1200px;overflow:hidden;background:var(--white)}
body{position:relative;font-family:"Open Sans",Arial,sans-serif;color:var(--body)}
.abs{position:absolute}

.masthead{left:0;top:0;width:908px;height:72px;background:var(--sky);display:flex;align-items:center;justify-content:center}
.masthead .brand{font-family:"Montserrat",Arial,sans-serif;font-weight:700;font-size:30px;color:var(--white);letter-spacing:.3px}

.main-nav{left:0;top:72px;width:908px;height:40px;background:var(--nav);display:flex;align-items:center;justify-content:center;gap:43px;padding-right:2px}
.main-nav a{font-size:11.5px;color:#bdbdbd;text-decoration:none;text-transform:uppercase}
.main-nav a.current{color:var(--white)}

.hero{left:0;top:112px;width:908px;height:333px;background:linear-gradient(100deg,#f4c7c9 0%,#e9b9cf 25%,#a7a7d8 55%,#6f92cf 80%,#6c8fd0 100%)}
.hero .headline{left:85px;top:118px;width:380px;font-size:21px;font-weight:700;line-height:25px;color:var(--ink);text-transform:uppercase}
.hero .lede{left:86px;top:175px;width:336px;font-size:9.6px;line-height:14px;color:var(--ink)}
.hero .pager{left:416px;top:298px;width:76px;height:16px;border-radius:8px;background:rgba(90,100,130,.55);display:flex;align-items:center;justify-content:center;gap:8px}
.hero .pager span{width:7px;height:7px;border-radius:50%;background:#e8e8f0}
.hero .pager span.on{background:transparent;border:1.4px solid #e8e8f0}

.welcome-title{left:77px;top:466px;font-size:21px;color:var(--accent);font-weight:400}
.welcome-text{left:77px;top:507px;width:562px;font-size:10.4px;line-height:17.4px;color:var(--body)}
.rule{height:1px;background:var(--rule)}

.topic{top:634px;width:181px}
.topic .thumb{width:181px;height:109px}
.topic h3{margin-top:7px;margin-left:1px;font-size:16px;font-weight:400;color:var(--accent)}
.topic p{margin-left:1px;font-size:9.3px;color:var(--muted)}

.side-title{left:651px;top:481px;font-size:16px;color:var(--accent);font-weight:400}
.quote-box{left:651px;top:513px;width:182px;height:230px;background:var(--panel);border:1px solid #ececec;padding:12px 14px;font-style:italic;font-size:9.7px;line-height:18.9px;color:var(--muted)}
.quote-tail{left:673px;top:742px}
.quote-name{left:652px;top:764px;font-size:10.4px;color:var(--muted)}
.quote-name b{color:#111;font-weight:600}

.blog-title{left:77px;top:849px;font-size:16px;color:var(--accent);font-weight:400}
.blog-arrows{left:799px;top:852px;display:flex;gap:2px}
.blog-arrows span{width:15px;height:15px;border-radius:50%;background:#e6e6e6;display:flex;align-items:center;justify-content:center}

.post{top:890px;width:364px;height:128px;border:1px solid #e4e4e4;display:flex}
.post .thumb{width:124px;height:126px;flex:none}
.post .body{padding:17px 0 0 18px}
.post h4{font-size:12.8px;font-weight:400;color:#555}
.post p{margin-top:6px;width:200px;font-size:9.3px;line-height:14.4px;color:var(--muted)}
.post .meta{margin-top:10px;display:flex;align-items:center;gap:22px;font-size:9.7px;color:var(--muted)}
.post .meta .icons{display:flex;gap:14px;align-items:center}

.site-footer{left:0;top:1058px;width:908px;height:142px;background:var(--footer)}
.footer-links{left:0;top:22px;width:908px;text-align:center;font-size:10.4px;color:#dcdcdc}
.footer-links .sep{color:#777;margin:0 7px}
.copyright{left:0;top:48px;width:908px;text-align:center;font-size:10.4px;color:#dcdcdc}
.social{left:0;top:81px;width:908px;display:flex;justify-content:center;gap:9px;padding-right:2px}
.social span{width:34px;height:34px;border-radius:50%;background:var(--white)}
</style>
</head>
<body>

<header class="masthead abs"><div class="brand">StillHarbor Way</div></header>

<nav class="main-nav abs">
  <a class="current">Home</a><a>Product</a><a>Success Stories</a><a>Anxiety Test</a><a>Blog</a><a>About</a><a>FAQ</a><a>Contact us</a>
</nav>

<section class="hero abs" role="img" aria-label="Photo of a joyful woman leaping with arms spread against a soft pink and blue sky">
  <h1 class="headline abs">Morbi rhoncus leoat finibus placerat molestie</h1>
  <p class="lede abs">Cum sociis natoque penatibus et magnis dis parturient montes, nascetur ridiculus mus. Nam eu gravida sem. Donec sem eros, ves tibulum sit amet fermentum eu, pretium ac nulla.</p>
  <div class="pager abs"><span class="on"></span><span></span><span></span><span></span></div>
</section>

<h2 class="welcome-title abs">Welcome to StillHarbor Way</h2>
<p class="welcome-text abs">Mauris mi sem, lacinia et tincidunt non, placerat vulputate nulla. In molestie risus vel elit rutrum condimentum. Nulla augue nulla, pulvinar eget ante vel, tempor elementum risus. Nulla nec gravida dolor, nec interdum lacus. Aliquam et sem vitae libero egestas facilisis. Morbi tempus augue eu turpis elementum lacinia. Vestibulum efficitur, erat eu commodo porta, ipsum nibh dictum ipsum, vel suscipit turpis ligula vel odio. Morbi rhoncus leo at placerat molestie. Maecenas finibus a elit eget dapibus.</p>
<div class="rule abs" style="left:76px;top:616px;width:560px"></div>

<article class="topic abs" style="left:76px">
  <div class="thumb" role="img" aria-label="Photo of a worried woman behind a rain-covered window" style="background:linear-gradient(180deg,#9ea4aa,#6d7176)"></div>
  <h3>Anxiety</h3><p>Morbi tempus augue eu turpis</p>
</article>
<article class="topic abs" style="left:265px">
  <div class="thumb" role="img" aria-label="Photo of a stressed blonde woman with raised hands" style="background:linear-gradient(120deg,#c9b9a6,#7d5a50)"></div>
  <h3>Panic Attacks</h3><p>Morbi tempus augue eu turpis</p>
</article>
<article class="topic abs" style="left:454px">
  <div class="thumb" role="img" aria-label="Photo of a sleepless woman lying in bed" style="background:linear-gradient(160deg,#7a6a5c,#d9d2c8)"></div>
  <h3>Other Disorders</h3><p>Morbi tempus augue eu turpis</p>
</article>

<h2 class="side-title abs">Success Stories</h2>
<blockquote class="quote-box abs">“ Cum sociis natoque penatibus et magnis dis parturient montes, nascetur ridiculus mus. Nam eu gravida sem. Donec sem eros, vestibulum sit amet fermentum eu, pretium ac nulla. Maecenas posuere dui in augue laoreet, eu consequat tortor gravida. Donec at lacus nunc consectetur adipi-scing elit. Sed rutrum interdum sem vitae elementum. ”</blockquote>
<svg class="quote-tail abs" width="16" height="9" viewBox="0 0 16 9"><path d="M0 0 L8 8 L16 0" fill="#f6f6f6" stroke="#ececec"/><path d="M1 0 H15" stroke="#f6f6f6" stroke-width="2"/></svg>
<p class="quote-name abs"><b>Ellis Grant,</b> Nulla nec gravida</p>

<div class="rule abs" style="left:76px;top:821px;width:757px"></div>
<h2 class="blog-title abs">Our Blog</h2>
<div class="blog-arrows abs">
  <span><svg width="6" height="8" viewBox="0 0 6 8"><path d="M4.5 1 L1.5 4 L4.5 7" fill="none" stroke="#555" stroke-width="1.3"/></svg></span>
  <span><svg width="6" height="8" viewBox="0 0 6 8"><path d="M1.5 1 L4.5 4 L1.5 7" fill="none" stroke="#555" stroke-width="1.3"/></svg></span>
</div>

<article class="post abs" style="left:78px">
  <div class="thumb" role="img" aria-label="Photo of a smiling businessman giving a thumbs up" style="background:linear-gradient(160deg,#8a8f93,#3a3b3d)"></div>
  <div class="body">
    <h4>Nam semper metus ac</h4>
    <p>Phasellus at magna gravida, viverra nulla quis, vestibulum purus. In hac habitasse platea dictumst. Nulla egestas augue eu est.</p>
    <div class="meta"><span>Oct 2, 2014</span><span class="icons">
      <svg width="11" height="9" viewBox="0 0 11 9"><path d="M0 2 H3 L7 7 H10 M0 7 H3 L7 2 H10" fill="none" stroke="#777" stroke-width="1.2"/><path d="M8.5 0.5 L10.5 2 L8.5 3.5 M8.5 5.5 L10.5 7 L8.5 8.5" fill="none" stroke="#777" stroke-width="1"/></svg>
      <svg width="9" height="8" viewBox="0 0 9 8"><path d="M0 0 H9 V5.5 H4 L2 8 V5.5 H0 Z" fill="#888"/></svg>
    </span></div>
  </div>
</article>
<article class="post abs" style="left:466px">
  <div class="thumb" role="img" aria-label="Photo of a man in white on a wooden pier by the sea" style="background:linear-gradient(180deg,#cfdce2,#a9a39a)"></div>
  <div class="body">
    <h4>Nam semper metus ac</h4>
    <p>Phasellus at magna gravida, viverra nulla quis, vestibulum purus. In hac habitasse platea dictumst. Nulla egestas augue eu est.</p>
    <div class="meta"><span>Oct 2, 2014</span><span class="icons">
      <svg width="11" height="9" viewBox="0 0 11 9"><path d="M0 2 H3 L7 7 H10 M0 7 H3 L7 2 H10" fill="none" stroke="#777" stroke-width="1.2"/><path d="M8.5 0.5 L10.5 2 L8.5 3.5 M8.5 5.5 L10.5 7 L8.5 8.5" fill="none" stroke="#777" stroke-width="1"/></svg>
      <svg width="9" height="8" viewBox="0 0 9 8"><path d="M0 0 H9 V5.5 H4 L2 8 V5.5 H0 Z" fill="#888"/></svg>
    </span></div>
  </div>
</article>

<footer class="site-footer abs">
  <p class="footer-links abs">Home<span class="sep">/</span>Product<span class="sep">/</span>Success Stories<span class="sep">/</span>Anxiety Test<span class="sep">/</span>Blog<span class="sep">/</span>About<span class="sep">/</span>FAQ<span class="sep">/</span>Contact us</p>
  <p class="copyright abs">Copyright ©&nbsp; 2014&nbsp; StillHarbor Way.&nbsp;&nbsp; All rights reserved.</p>
  <div class="social abs"><span></span><span></span><span></span><span></span><span></span><span></span></div>
</footer>

</body>
</html>
```